Quillfern Nightclub Flyer (Updated)

Flyer for facebook, square is fine, or rectangular. Here is the text:
QUILLFERN
Nightclub + Lounge
presents

SPLIT DECK WEDNESDAY
Nov 29 2018

CLUB FLOOR:
GORDY B2B RALPH
THEODORE BRUSKVIK

LOUNGE:
OTIS B2B HALF TIDE
COPPER FENWICK

Powered by HALVERN Acoustics
4716 Larchmere Avenue 21+ 9pm-2am
quillfernvenue-example.com for VIP booth inquiries

Target Market(s)

Nightclub

Industry/Entity Type

Night Club

Font styles to use
Sans Serif

Colors

Designer to choose colors to be used in the design.

Requirements
Must have
• All the text listed, and plz keep the theme of the attached files. We want to stay consistent with the Quillfern brand
Nice to have
• Try to stay with the theme from the attachments
Should not have
• Dont' stray to far from the general theme we have from the attachments

```html
<!DOCTYPE html>
<html lang="en">
<head>
<meta charset="utf-8">
<title>Quillfern Nightclub + Lounge — Split Deck Wednesday</title>
<link rel="stylesheet" href="https://fonts.googleapis.com/css2?family=Bodoni+Moda:wght@400;600;700&family=Montserrat:wght@300;400;500;700&display=swap">
<style>
  :root {
    --ink: #000000;
    --white: #ffffff;
    --gold: #c9a46a;
    --gold-light: #e6c48e;
    --gold-deep: #a9824a;
    --rule: #8a7150;
    --serif: "Bodoni Moda", "Didot", serif;
    --sans: "Montserrat", "Helvetica Neue", sans-serif;
  }
  * { margin: 0; padding: 0; box-sizing: border-box; }
  html, body { width: 1200px; height: 1200px; overflow: hidden; background: var(--ink); }
  .flyer { position: relative; width: 1200px; height: 1200px; background: var(--ink); overflow: hidden; color: var(--white); }

  .brand { position: absolute; top: 82px; left: 0; width: 100%; text-align: center; }
  .brand-name { font-family: var(--serif); font-weight: 400; font-size: 104px; line-height: 1; letter-spacing: 1px; }
  .brand-sub { margin-top: 14px; font-family: var(--sans); font-weight: 300; font-size: 28px; letter-spacing: 5px; }

  .presents-badge {
    position: absolute; top: 297px; left: 50%; transform: translateX(-50%);
    padding: 6px 16px; background: linear-gradient(90deg, var(--gold-deep), var(--gold-light) 50%, var(--gold-deep));
    font-family: var(--sans); font-weight: 700; font-size: 19px; letter-spacing: 0.5px; color: #1a1208;
  }

  .event { position: absolute; top: 382px; left: 0; width: 100%; text-align: center; }
  .event-title { font-family: var(--serif); font-weight: 700; font-size: 58px; line-height: 1; letter-spacing: 1.5px; }
  .event-date { margin-top: 22px; font-family: var(--sans); font-weight: 300; font-size: 62px; line-height: 1; }

  .mandala-area {
    position: absolute; left: -264px; top: 588px; width: 696px; height: 696px; border-radius: 50%;
    background: radial-gradient(circle, #3a2c18 0%, #7a5d33 35%, #b8925a 60%, #6a4f2a 80%, rgba(0,0,0,0) 100%);
  }

  .lineup { position: absolute; left: 603px; width: 465px; }
  .lineup-heading { font-family: var(--serif); font-weight: 700; font-size: 44px; line-height: 1; letter-spacing: 0.5px; }
  .lineup-rule { position: relative; display: block; margin-top: 14px; height: 10px; }
  .lineup-acts { list-style: none; margin-top: 34px; font-family: var(--sans); font-weight: 500; font-size: 22px; letter-spacing: 0.6px; line-height: 39px; }
  .lineup--club { top: 626px; }
  .lineup--lounge { top: 830px; }

  .venue-info {
    position: absolute; right: 72px; top: 1079px; text-align: right;
    font-family: var(--sans); font-weight: 400; font-size: 18px; line-height: 23px; letter-spacing: 1.6px; color: var(--gold);
  }
</style>
</head>
<body>
<main class="flyer">
  <header class="brand">
    <h1 class="brand-name">QUILLFERN</h1>
    <p class="brand-sub">NIGHTCLUB + LOUNGE</p>
  </header>

  <div class="presents-badge">PRESENTS</div>

  <section class="event">
    <h2 class="event-title">SPLIT DECK WEDNESDAY</h2>
    <p class="event-date">Nov 29 2018</p>
  </section>

  <div class="mandala-area" role="img" aria-label="Decorative gold mandala ornament"></div>

  <section class="lineup lineup--club">
    <h3 class="lineup-heading">Club Floor</h3>
    <svg class="lineup-rule" width="465" height="10" viewBox="0 0 465 10" aria-hidden="true">
      <line x1="0" y1="5" x2="440" y2="5" stroke="var(--rule)" stroke-width="1.2"/>
      <circle cx="448" cy="5" r="3" fill="none" stroke="var(--gold)" stroke-width="1"/>
    </svg>
    <ul class="lineup-acts">
      <li>GORDY B2B RALPH</li>
      <li>THEODORE BRUSKVIK</li>
    </ul>
  </section>

  <section class="lineup lineup--lounge">
    <h3 class="lineup-heading">Lounge</h3>
    <svg class="lineup-rule" width="465" height="10" viewBox="0 0 465 10" aria-hidden="true">
      <line x1="0" y1="5" x2="440" y2="5" stroke="var(--rule)" stroke-width="1.2"/>
      <circle cx="448" cy="5" r="3" fill="none" stroke="var(--gold)" stroke-width="1"/>
    </svg>
    <ul class="lineup-acts">
      <li>OTIS B2B HALF TIDE</li>
      <li>COPPER FENWICK</li>
    </ul>
  </section>

  <footer class="venue-info">
    <p>POWERED BY HALVERN ACOUSTICS</p>
    <p>4716 LARCHMERE AVENUE 21+ 9PM-2AM</p>
    <p>QUILLFERNVENUE-EXAMPLE.COM FOR VIP BOOTH INQUIRIES</p>
  </footer>
</main>
</body>
</html>
```